Bikes for Dreams - Website Redesign

Create a professional website for a nonprofit; BikesforDreams.org
Please see boatsforheroes.org and www.pedalsforhopes.org for the concept I am after.
The webpage should have a fun feel and should match the style of the company at www.pedalsforhopes.org. The pages to include are 'Home', 'About us' and 'Get Started'
Thank you and good luck!
Reason: i would like to see more designs.

```html
<!DOCTYPE html>
<html lang="en">
<head>
<meta charset="utf-8">
<title>Bikes for Dreams</title>
<link href="https://fonts.googleapis.com/css2?family=Lato:wght@300;400;700&display=swap" rel="stylesheet">
<style>
:root{
  --blue:#1a8ad4;
  --blue-dark:#1f6fb5;
  --band:#2a5fa8;
  --navy:#1b5ea6;
  --orange:#ef8a2b;
  --orange-soft:#f0a54b;
  --text:#555;
  --muted:#888;
  --line:#d9dde2;
  --paper:#f6f6f6;
  --white:#fff;
}
*{box-sizing:border-box;margin:0;padding:0}
html,body{width:1200px;height:3285px;overflow:hidden}
body{font-family:'Lato',sans-serif;color:var(--text);background:var(--white);position:relative}

/* header */
.site-header{position:absolute;top:0;left:0;width:1200px;height:103px;background:var(--white)}
.brand{position:absolute;left:79px;top:34px;display:flex;align-items:center;gap:10px;font-size:28px;font-weight:700;color:var(--orange)}
.brand-dot{width:22px;height:22px;border-radius:50%;background:var(--orange)}
.nav{position:absolute;top:30px;left:500px;display:flex;align-items:center;font-size:15px;color:#555}
.nav a{color:inherit;text-decoration:none;margin-right:40px}
.nav .pill{border:2px solid var(--orange);color:var(--orange);border-radius:24px;padding:10px 20px;margin-right:30px}
.nav .divider{width:1px;height:44px;background:var(--line);margin-right:30px}
.nav .phone{display:flex;align-items:center;gap:12px;color:#777}
.nav .phone b{color:var(--blue);font-weight:700}

/* hero */
.hero{position:absolute;top:103px;left:0;width:1200px;height:576px;background:linear-gradient(180deg,#cfe6f5 0%,#e7f2fa 55%,#b9d2e6 75%,#9fc46e 85%,#9aa3ab 100%)}
.hero h1{position:absolute;left:79px;top:75px;font-size:56px;line-height:60px;font-weight:400;color:var(--navy)}
.hero .sub{position:absolute;left:81px;top:220px;font-size:30px;font-weight:300;color:#4a5b6c}
.btn{background:var(--orange);color:var(--white);font-weight:700;text-transform:uppercase;display:flex;align-items:center;justify-content:center;border-radius:3px}
.hero-cta{position:absolute;left:79px;top:285px;width:208px;height:48px;font-size:22px;font-weight:400}
.quick-form{position:absolute;left:810px;top:37px;width:311px;height:517px;background:rgba(70,160,225,.85);padding:14px 20px}
.quick-form h2{text-align:center;color:var(--white);font-weight:400;font-size:31px;margin-bottom:12px}
.field{background:var(--white);height:50px;border-radius:3px;margin-bottom:8px;display:flex;align-items:center;justify-content:space-between;padding:0 22px;font-size:13px;color:#999;border:1px solid var(--line)}
.quick-form .field{height:49px;margin-bottom:8px}
.quick-form .submit{height:52px;font-size:22px;font-weight:400;margin-top:20px}

/* steps */
.section-title{text-align:center;font-weight:400;font-size:38px;color:var(--blue)}
.steps{position:absolute;top:679px;left:0;width:1200px;height:449px}
.steps .section-title{margin-top:48px}
.step{position:absolute;top:103px;width:320px;text-align:center}
.step-ring{width:220px;height:220px;border-radius:50%;background:var(--white);box-shadow:0 0 14px rgba(0,0,0,.12);margin:0 auto;display:flex;align-items:center;justify-content:center}
.step-core{width:170px;height:170px;border-radius:50%;background:var(--blue);display:flex;align-items:center;justify-content:center}
.step p{margin-top:22px;font-size:17px;line-height:28px;color:#555}

/* donate types */
.types{position:absolute;top:1128px;left:0;width:1200px;height:383px;background:var(--blue)}
.types .section-title{color:var(--white);margin-top:50px}
.type{position:absolute;top:120px;width:234px;text-align:center;color:var(--white);font-size:15px;line-height:25px}
.type .pic{height:154px;margin-bottom:22px;border:4px solid var(--white)}
.donate-band{position:absolute;top:1511px;left:0;width:1200px;height:53px;background:var(--band);color:var(--white);font-size:21px;display:flex;align-items:center;justify-content:center;letter-spacing:1px}

/* mission */
.mission{position:absolute;top:1564px;left:0;width:1200px;height:385px}
.mission .section-title{margin-top:52px}
.mission p{width:720px;margin:18px auto 0;text-align:center;font-size:15.5px;line-height:26px;color:#555}
.counter{position:absolute;top:254px;left:302px;display:flex;align-items:center;gap:6px}
.digit{width:60px;height:70px;background:linear-gradient(180deg,#fff 0%,#f1f1f1 49%,#dedede 51%,#ececec 100%);border:1px solid #ccc;color:var(--navy);font-size:50px;display:flex;align-items:center;justify-content:center}
.counter .comma{color:var(--navy);font-size:50px;margin:0 -2px}

/* stars */
.stars{position:absolute;top:1949px;left:0;width:1200px;height:388px;background:var(--orange-soft)}
.stars .section-title{color:var(--white);margin-top:50px}
.star{position:absolute;top:127px;width:206px;height:206px;border-radius:50%;border:4px solid var(--white)}
.star.cta{background:var(--white);display:flex;align-items:center;justify-content:center;text-align:center;font-size:30px;font-weight:300;color:#777;line-height:34px}

/* reasons + form */
.reasons{position:absolute;top:2337px;left:0;width:1200px;height:637px;background:var(--paper)}
.reasons .section-title{margin-top:48px}
.reason{position:absolute;top:134px;display:flex;gap:14px;font-size:15px;line-height:24px;color:#555}
.form-card{position:absolute;top:230px;left:131px;width:938px;height:407px;background:var(--white);border:1px solid #e4e4e4;border-bottom:none}
.form-card h2{text-align:center;font-weight:400;font-size:38px;color:var(--blue);margin-top:28px}
.form-card .lead{text-align:center;font-size:17px;color:var(--muted);margin-top:12px}
.form-grid{position:absolute;top:149px;left:42px;display:grid;grid-template-columns:272px 272px 272px;column-gap:19px;row-gap:22px}
.form-grid .field{height:52px;margin:0}
.form-grid .submit{height:52px;font-size:22px;font-weight:400}

/* footer */
.site-footer{position:absolute;top:2974px;left:0;width:1200px;height:311px;background:var(--blue);color:var(--white)}
.site-footer h3{font-weight:400;font-size:21px}
.foot-about{position:absolute;left:79px;top:40px;width:410px}
.foot-about p{margin-top:20px;font-size:14px;line-height:25px}
.foot-map{position:absolute;left:569px;top:40px}
.foot-map ul{list-style:none;margin-top:16px;font-size:14px;line-height:32px}
.foot-brand{position:absolute;left:860px;top:92px;font-size:26px;font-weight:700}
.socials{position:absolute;left:823px;top:140px;display:flex;gap:12px}
.socials span{width:40px;height:40px;border-radius:50%;background:var(--white)}
.foot-rule{position:absolute;left:79px;top:250px;width:1042px;height:1px;background:rgba(255,255,255,.35)}
.copy{position:absolute;left:0;top:270px;width:1200px;text-align:center;font-size:15px}
.copy b{color:var(--orange);font-weight:400}
</style>
</head>
<body>

<header class="site-header">
  <div class="brand"><span class="brand-dot"></span>Bikes for Dreams</div>
  <nav class="nav">
    <a href="#">Home</a>
    <a href="#">About Us</a>
    <a href="#" class="pill">Get Started</a>
    <span class="divider"></span>
    <span class="phone">
      <svg width="20" height="20" viewBox="0 0 24 24"><path d="M6.6 10.8a15 15 0 0 0 6.6 6.6l2.2-2.2a1 1 0 0 1 1-.25 11.4 11.4 0 0 0 3.6.57 1 1 0 0 1 1 1V20a1 1 0 0 1-1 1A17 17 0 0 1 3 4a1 1 0 0 1 1-1h3.5a1 1 0 0 1 1 1c0 1.25.2 2.45.57 3.6a1 1 0 0 1-.25 1z" fill="none" stroke="#ef8a2b" stroke-width="1.6"/></svg>
      Call toll-free <b>1-888-555-0142</b>
    </span>
  </nav>
</header>

<section class="hero" role="img" aria-label="Illustrated city skyline with a tow truck carrying a red car and a woman beside a warning triangle">
  <h1>We do the Work. You<br>Enjoy the Tax Benefits!</h1>
  <div class="sub">Les Hassle, more Happiness.</div>
  <div class="btn hero-cta">Donate Now</div>
  <form class="quick-form">
    <h2>Donating is Simple</h2>
    <div class="field">Vehicle Type
      <svg width="14" height="10" viewBox="0 0 14 10"><path d="M2 2l5 5 5-5" fill="none" stroke="#555" stroke-width="2"/></svg>
    </div>
    <div class="field">Full Name</div>
    <div class="field">Phone Number</div>
    <div class="field">Email</div>
    <div class="field">Pick Up Address</div>
    <div class="field">Zipcode</div>
    <div class="btn submit">Donate Now</div>
  </form>
</section>

<section class="steps">
  <h2 class="section-title">Car Donation</h2>
  <div class="step" style="left:94px">
    <div class="step-ring"><div class="step-core">
      <svg width="90" height="60" viewBox="0 0 90 60"><path d="M10 34l10-20c2-4 5-6 9-6h32c4 0 7 2 9 6l10 20v16H10z" fill="#fff"/><rect x="22" y="14" width="46" height="14" rx="3" fill="#1a8ad4"/><rect x="14" y="50" width="12" height="8" fill="#fff"/><rect x="64" y="50" width="12" height="8" fill="#fff"/><circle cx="22" cy="40" r="4" fill="#1a8ad4"/><circle cx="68" cy="40" r="4" fill="#1a8ad4"/></svg>
    </div></div>
    <p>Call Us at 1-888-555-0142 or Fill The<br>Form to Donate Your Vehicle.</p>
  </div>
  <div class="step" style="left:440px">
    <div class="step-ring"><div class="step-core">
      <svg width="100" height="70" viewBox="0 0 100 70"><rect x="6" y="32" width="62" height="22" fill="#fff"/><path d="M68 30h16l10 12v12H68z" fill="#fff"/><path d="M12 30l8-12h30l8 12z" fill="#fff"/><circle cx="22" cy="58" r="8" fill="#fff" stroke="#1a8ad4" stroke-width="3"/><circle cx="80" cy="58" r="8" fill="#fff" stroke="#1a8ad4" stroke-width="3"/></svg>
    </div></div>
    <p>We Tow the Vehicle From AnyWhere in<br>Same Day to 24 Hours.</p>
  </div>
  <div class="step" style="left:786px">
    <div class="step-ring"><div class="step-core">
      <svg width="70" height="64" viewBox="0 0 70 64"><path d="M35 60C10 42 4 30 4 20A15 15 0 0 1 35 12a15 15 0 0 1 31 8c0 10-6 22-31 40z" fill="#fff"/></svg>
    </div></div>
    <p>Help Local Children By Donating Your<br>Vehicle &amp; Get Tax Deduction Receipt.</p>
  </div>
</section>

<section class="types">
  <h2 class="section-title">What can be Donated</h2>
  <div class="type" style="left:109px"><div class="pic" role="img" aria-label="Illustration of a yellow car" style="background:linear-gradient(180deg,#fff 60%,#f6c73a 60%,#f6c73a 80%,#ddd 80%)"></div>Donate your car &amp; help local<br>children's charities</div>
  <div class="type" style="left:359px"><div class="pic" role="img" aria-label="Illustration of a motor boat on water" style="background:linear-gradient(180deg,#fff 50%,#e8553b 50%,#e8553b 70%,#3fa0e0 70%)"></div>Bikes For Dreams Accepts Boats<br>Too!</div>
  <div class="type" style="left:609px"><div class="pic" role="img" aria-label="Illustration of a red motorcycle" style="background:linear-gradient(180deg,#fff 45%,#c9302c 45%,#c9302c 72%,#fff 72%,#fff 85%,#ddd 85%)"></div>Learn About Donating A<br>Motorcycle</div>
  <div class="type" style="left:858px"><div class="pic" role="img" aria-label="Illustration of a teal camper van" style="background:linear-gradient(180deg,#fff 35%,#6cc5c0 35%,#6cc5c0 78%,#ddd 78%)"></div>Discover How to Donate Your<br>Old RV or Motorhome</div>
</section>
<div class="donate-band">DONATE NOW</div>

<section class="mission">
  <h2 class="section-title">Our Mission</h2>
  <p>Lorem Ipsum is simply dummy text of the printing and typesetting industry. Lorem Ipsum has been the industry's standard dummy text ever since the 1500s, when an unknown printer took a galley of type and scrambled it to make a type specimen book. It has survived not only five centuries, but also the leap into electronic typesetting, remaining essentially unchanged.</p>
  <div class="counter">
    <span class="digit">$</span><span class="digit">4</span><span class="digit">1</span><span class="comma">,</span><span class="digit">4</span><span class="digit">8</span><span class="digit">2</span><span class="comma">,</span><span class="digit">7</span><span class="digit">6</span><span class="digit">1</span>
  </div>
</section>

<section class="stars">
  <h2 class="section-title">The Stars of Bikes For Dreams!</h2>
  <div class="star" style="left:37px;background:linear-gradient(135deg,#e9eef2,#7fb3d6)" role="img" aria-label="Photo of a child with a doctor"></div>
  <div class="star" style="left:267px;background:linear-gradient(135deg,#3c4a5a,#e3ddd4)" role="img" aria-label="Photo of a boy hugging a white puppy"></div>
  <div class="star" style="left:497px;background:linear-gradient(135deg,#b5a39a,#d9665f)" role="img" aria-label="Photo of a mother hugging her child"></div>
  <div class="star" style="left:729px;background:linear-gradient(135deg,#c7d9e8,#e8d6c4)" role="img" aria-label="Photo of a girl holding a teddy bear"></div>
  <div class="star cta" style="left:955px">Make a<br>Difference...</div>
</section>

<section class="reasons">
  <h2 class="section-title">Still Need a Reason?</h2>
  <div class="reason" style="left:105px"><svg width="44" height="40" viewBox="0 0 44 40"><circle cx="18" cy="22" r="15" fill="none" stroke="#888" stroke-width="2"/><path d="M10 21l7 8L40 4" fill="none" stroke="#d9322b" stroke-width="4"/></svg><span>Your donation helps kids<br>in your local community</span></div>
  <div class="reason" style="left:367px"><svg width="44" height="40" viewBox="0 0 44 40"><circle cx="18" cy="22" r="15" fill="none" stroke="#888" stroke-width="2"/><path d="M10 21l7 8L40 4" fill="none" stroke="#d9322b" stroke-width="4"/></svg><span>No time or money wasted<br>selling your vehicle</span></div>
  <div class="reason" style="left:630px"><svg width="44" height="40" viewBox="0 0 44 40"><circle cx="18" cy="22" r="15" fill="none" stroke="#888" stroke-width="2"/><path d="M10 21l7 8L40 4" fill="none" stroke="#d9322b" stroke-width="4"/></svg><span>Accepting all vehicles in<br>any condition</span></div>
  <div class="reason" style="left:892px"><svg width="44" height="40" viewBox="0 0 44 40"><circle cx="18" cy="22" r="15" fill="none" stroke="#888" stroke-width="2"/><path d="M10 21l7 8L40 4" fill="none" stroke="#d9322b" stroke-width="4"/></svg><span>We do all the work!</span></div>

  <form class="form-card">
    <h2>Donating is Simple</h2>
    <div class="lead">Let us know the details of your home and we'll toll your vehicle for Donation</div>
    <div class="form-grid">
      <div class="field">Vehicle Type <svg width="14" height="10" viewBox="0 0 14 10"><path d="M2 2l5 5 5-5" fill="none" stroke="#555" stroke-width="2"/></svg></div>
      <div class="field">Full Name</div>
      <div class="field">Phone Number</div>
      <div class="field">Email</div>
      <div class="field">Pick Up Address</div>
      <div class="field">State</div>
      <div class="field">City <svg width="14" height="10" viewBox="0 0 14 10"><path d="M2 2l5 5 5-5" fill="none" stroke="#555" stroke-width="2"/></svg></div>
      <div class="field">Zipcode</div>
      <div class="btn submit">Donate Now</div>
    </div>
  </form>
</section>

<footer class="site-footer">
  <div class="foot-about">
    <h3>Bikes For Dreams</h3>
    <p>Lorem Ipsum is simply dummy text of the printing and typesetting industry. Lorem Ipsum has been the industry's standard dummy text ever since the 1500s, when an unknown printer took a galley of type and scrambled it to make a type specimen book.</p>
  </div>
  <div class="foot-map">
    <h3>Site Map</h3>
    <ul><li>Home</li><li>About Us</li><li>Get Started</li><li>Privacy Policy</li></ul>
  </div>
  <div class="foot-brand">Bikes for Dreams</div>
  <div class="socials"><span></span><span></span><span></span><span></span><span></span><span></span></div>
  <div class="foot-rule"></div>
  <div class="copy">© <b>Bikes For Dreams</b> - 2017. All Rights Reserved.</div>
</footer>

</body>
</html>
```